Stationery for Villa Marisol Design Hotel**

Who we are:

Wander on an isolated beach while breathing in the fresh, salty, sea air. Listen to the warm Pacific wind rustling through green palm trees as you walk to a pristine lagoon. Feel the delicious warmth of the sun kiss your skin; the beach is yours. At Villa Marisol you can experience a vacation in undisturbed, natural beauty. We have created a place for you to find new strength, relaxation, and inner harmony. We offer total rest to the experienced traveler from all over the world.

We are a brand new and smartly built design-hotel (under construction) close to a unique beach and a fantastic surf spot in Huatulco, Southwest Mexico.

As you can see in the attachments, we do have an established corporate design, but as for now still need a format for booklets for information around our hotel and things to do in the area, important numbers (we fill in the content for that one).

Our corporate colors:
green #64b445, brown #b07043, blue #0ab7cf, yellow # f9b02a and #fcc01a, navy #444f69
Corporate fonts:
Krub and Miller Banner.
For further information access:
www.villamarisol-example.mx
https://slidevault.example/view/QmWpLxTe8HnKdYcRuZsJ/

Social Media: VillaMarisol

Industry/Entity Type

Hotel

Font styles to use
Other font styles liked:
• Krub, Miller Banner

Requirements
Must have
• Stick to Logo Design, defined corporate elements, logo, colors, fonts and general touch and feel
Nice to have
• Who we are:

Our corporate colors:
Corporate fonts:
Krub and Miller Banner.
www.villamarisol-example.mx

Social Media: VillaMarisol

```html
<!DOCTYPE html>
<html lang="en">
<head>
<meta charset="utf-8">
<title>Villa Marisol – Letterhead</title>
<link rel="stylesheet" href="https://fonts.googleapis.com/css2?family=Krub:wght@400;500;600&family=Open+Sans:wght@400&display=swap">
<style>
  :root {
    --backdrop: #dcdcdc;
    --paper: #f8f8f8;
    --body-text: #474747;
    --navy: #444f69;
    --green: #64b445;
    --gold-deep: #d9a12a;
    --signature-tone: #e4e4e4;
  }
  * { margin: 0; padding: 0; box-sizing: border-box; }
  html, body {
    width: 1153px;
    height: 1200px;
    overflow: hidden;
    background: var(--backdrop);
  }
  .letterhead {
    position: absolute;
    left: 146px;
    top: 0;
    width: 860px;
    height: 1200px;
    background: var(--paper);
    box-shadow: 0 6px 24px rgba(0, 0, 0, 0.12);
  }
  .brand {
    position: absolute;
    left: 86px;
    top: 73px;
    width: 119px;
    display: flex;
    flex-direction: column;
    align-items: center;
  }
  .brand-square {
    width: 119px;
    height: 115px;
    border: 3px solid var(--gold-deep);
  }
  .brand-name {
    margin-top: 10px;
    font-family: "Krub", sans-serif;
    font-weight: 500;
    font-size: 17px;
    letter-spacing: 0.5px;
    color: var(--gold-deep);
    white-space: nowrap;
  }
  .letter {
    position: absolute;
    left: 77px;
    top: 303px;
    width: 705px;
    font-family: "Open Sans", sans-serif;
    font-size: 15.7px;
    line-height: 23.1px;
    color: var(--body-text);
  }
  .letter p { margin-bottom: 23.1px; }
  .letter .body-paragraph { text-align: justify; }
  .signature {
    width: 102px;
    height: 92px;
    margin-top: 4px;
    background: var(--signature-tone);
    border-radius: 4px;
  }
  .contact-footer {
    position: absolute;
    left: 0;
    right: 0;
    top: 1053px;
    text-align: center;
    font-family: "Krub", sans-serif;
    font-size: 18px;
    line-height: 27px;
    color: var(--navy);
    white-space: nowrap;
  }
  .contact-footer .label {
    color: var(--green);
    font-weight: 600;
    margin-left: 12px;
  }
  .contact-footer .label:first-child { margin-left: 0; }
</style>
</head>
<body>
  <main class="letterhead">
    <header class="brand">
      <div class="brand-square"></div>
      <div class="brand-name">Villa Marisol</div>
    </header>

    <section class="letter">
      <p>Dear customer,</p>
      <p class="body-paragraph">Lorem ipsum dolor sit amet, consectetur adipisicing elit, sed do eiusmod tempor incididunt ut labore et dolore magna aliqua. Ut enim ad minim veniam, quis nostrud exercitation ullamco laboris nisi ut aliquip ex ea commodo consequat. Duis aute irure dolor in reprehenderit in voluptate velit esse cillum dolore eu fugiat nulla pariatur. Excepteur sint occaecat cupidatat non proident, sunt in culpa qui officia deserunt mollit anim id est laborum.</p>
      <p class="body-paragraph">Lorem ipsum dolor sit amet, consectetur adipisicing elit, sed do eiusmod tempor incididunt ut labore et dolore magna aliqua. Ut enim ad minim veniam, quis nostrud exercitation ullamco laboris nisi ut aliquip ex ea commodo consequat. Duis aute irure dolor in reprehenderit in voluptate velit esse cillum dolore eu fugiat nulla pariatur. Excepteur sint occaecat cupidatat non proident, sunt in culpa qui officia deserunt mollit anim id est laborum.</p>
      <p class="body-paragraph">Lorem ipsum dolor sit amet, consectetur adipisicing elit, sed do eiusmod tempor incididunt ut labore et dolore magna aliqua. Ut enim ad minim veniam, quis nostrud exercitation ullamco laboris nisi ut aliquip ex ea commodo consequat. Duis aute irure dolor in reprehenderit in voluptate velit esse cillum dolore eu fugiat nulla pariatur. Excepteur sint occaecat cupidatat non proident, sunt in culpa qui officia deserunt mollit anim id est laborum.</p>
      <p class="body-paragraph">Lorem ipsum dolor sit amet, consectetur adipisicing elit, sed do eiusmod tempor incididunt ut labore et dolore magna aliqua. Ut enim ad minim veniam, quis nostrud exercitation ullamco laboris nisi ut aliquip ex ea commodo consequat. Duis aute irure dolor in reprehenderit.</p>
      <p>Yours Sincerely,</p>
      <div class="signature" role="img" aria-label="Handwritten signature of the sender"></div>
    </section>

    <footer class="contact-footer">
      <div class="address">Playa Serena, Bahía Clara, Costa del Sol</div>
      <div class="contact-line"><span class="label">T :</span> +00 1 (555) 010 0142 <span class="label">E :</span> hello@villamarisol-example.mx <span class="label">W :</span> www.villamarisol-example.mx</div>
    </footer>
  </main>
</body>
</html>
```